Fitness & sports performance company needs a landing page design

Looking for a landing page for a fitness & sports performance company based in South Florida. The company is 'The Lantern Athletic Club', and 'The Lantern' for short. The main objective of the landing page is to generate leads, and show potential clients the services we offer, as well as pricing for each service. While we are based in South Florida, we also offer online services such as an online trainer and online strength & conditioning programs. Would like to see designs that utilize the colors in our logo.

Target Market(s)

those looking to lose weight, gain strength and make overall healthy lifestyle changes

Font styles to use
Sans Serif

Colors
60b9df
57b5de

Requirements
Must have
• a place to list testimonials, list of services provided, show pricing for each service, colors of the website matching colors in the logo
Nice to have
• i would like to see a landing page that can be utilized to create leads and an email list

```html
<!DOCTYPE html>
<html lang="en">
<head>
<meta charset="utf-8">
<title>The Lantern Athletic Club</title>
<link rel="stylesheet" href="https://fonts.googleapis.com/css2?family=Montserrat:wght@400;500;600;700&family=Merriweather:wght@400;700&display=swap">
<style>
:root{
  --teal:#3cc3cc;
  --teal-dark:#2fb0b9;
  --ink:#1f2430;
  --body:#7a7f8a;
  --muted:#a3a7b0;
  --grad-a:#74c6f7;
  --grad-b:#6a63f4;
  --lavender:#d9d2fb;
  --white:#ffffff;
}
*{box-sizing:border-box;margin:0;padding:0}
html,body{width:1200px;height:3696px;overflow:hidden;background:var(--white)}
body{position:relative;font-family:"Montserrat",sans-serif;color:var(--ink)}
.abs{position:absolute}
.btn{display:inline-block;font-size:10px;font-weight:700;letter-spacing:1.5px;text-transform:uppercase;padding:12px 22px;border-radius:3px}
.btn-teal{background:var(--teal);color:var(--white)}
.btn-ghost{border:2px solid var(--white);color:var(--white)}
.eyebrow{font-size:10px;letter-spacing:2px;text-transform:uppercase;color:var(--muted);text-align:center}
.section-title{font-size:24px;font-weight:700;text-align:center}

/* hero */
.hero{left:0;top:0;width:1200px;height:665px;overflow:hidden}
.hero-photo{position:absolute;inset:0;background:radial-gradient(ellipse at 55% 20%,#d8c98e 0%,#7c8a55 35%,#3a4a2c 70%,#22301c 100%)}
.hero-shade{position:absolute;inset:0;background:rgba(20,25,20,.35)}
.hero-wave{position:absolute;left:0;top:0}
.nav{top:20px;left:30px;right:30px;height:30px}
.brand{left:0;top:2px;display:flex;align-items:center;gap:8px;color:var(--white);font-weight:700;font-size:13px}
.brand-dot{width:22px;height:22px;border-radius:50%;background:var(--teal)}
.nav-links{right:0;top:0;display:flex;align-items:center;gap:34px;font-size:11px;color:var(--white)}
.nav-links .btn{padding:9px 16px;font-size:9px;border-radius:16px}
.hero-title{top:210px;left:0;width:1200px;text-align:center;font-family:"Merriweather",serif;font-size:40px;color:var(--white);font-weight:400}
.hero-sub{top:278px;left:360px;width:480px;text-align:center;font-size:13px;line-height:20px;color:var(--white)}
.hero-cta{top:338px;left:0;width:1200px;display:flex;justify-content:center;gap:14px}

/* about */
.about-title{left:241px;top:826px;width:360px;font-size:22px;font-weight:700;line-height:32px}
.about-rule{left:241px;top:912px;width:40px;height:2px;background:var(--teal)}
.about-text{left:241px;width:345px;font-size:10.5px;line-height:17px;color:var(--body)}
.about-frame{left:697px;top:779px;width:284px;height:309px;border:3px solid var(--teal)}
.about-photo{left:670px;top:804px;width:290px;height:315px;background:linear-gradient(180deg,#c9ccc4 0%,#8e8a72 40%,#4b5a45 75%,#2d3a2e 100%);box-shadow:0 20px 40px rgba(0,0,0,.25)}

/* services */
.services-band{left:0;top:1220px}
.services-head{top:1385px;left:0;width:1200px}
.services-head .eyebrow{color:rgba(255,255,255,.8)}
.services-head .section-title{color:var(--white);margin-top:6px}
.card{width:226px;height:246px;background:var(--white);box-shadow:0 6px 16px rgba(40,40,90,.15);text-align:center;overflow:hidden}
.card-tab{position:absolute;left:96px;top:-17px;width:34px;height:34px;border-radius:50%;background:var(--teal)}
.card-icon{position:absolute;left:97px;top:50px}
.card h3{position:absolute;left:0;right:0;top:105px;font-size:13px;font-weight:700}
.card p{position:absolute;left:20px;right:20px;top:138px;font-size:9.5px;line-height:15px;color:var(--body)}

/* testimonials */
.testi-box{left:241px;top:2156px;width:717px;height:308px;border:2px solid var(--teal)}
.testi-head{left:475px;top:2126px;width:250px;background:var(--white)}
.testi-head .section-title{margin-top:6px}
.quote-mark{left:0;width:1200px;top:2212px;text-align:center;font-family:"Merriweather",serif;font-size:40px;font-weight:700;line-height:30px}
.testi-lead{left:0;width:1200px;top:2255px;text-align:center;font-size:13px;font-weight:600}
.testi-text{left:300px;width:600px;top:2290px;text-align:center;font-size:9.5px;line-height:16px;color:var(--body)}
.avatar{left:585px;top:2374px;width:30px;height:30px;border-radius:50%;background:linear-gradient(135deg,#8c7c6b,#4d5663)}
.testi-name{left:0;width:1200px;top:2414px;text-align:center;font-size:9.5px;color:var(--ink)}
.testi-name span{color:var(--teal)}

/* pricing */
.price-card{top:2760px;height:364px;background:var(--white);box-shadow:0 10px 24px rgba(0,0,0,.08);border-top:2px solid var(--teal);text-align:center}
.price-card.featured{top:2745px;height:397px;background:var(--teal);border-top:none;color:var(--white);box-shadow:0 10px 30px rgba(60,195,204,.35)}
.plan{margin-top:30px;font-size:9px;font-weight:600;letter-spacing:1.5px;color:var(--teal);text-transform:uppercase}
.featured .plan{color:var(--white)}
.amount{margin-top:8px;font-size:34px;font-weight:500;line-height:40px}
.amount sup{font-size:14px;vertical-align:top;line-height:22px}
.per{font-size:8.5px;color:var(--muted)}
.featured .per{color:var(--white)}
.divider{height:1px;background:#eceef1;margin:24px 0 26px}
.featured .divider{background:rgba(255,255,255,.35)}
.features{list-style:none;font-size:9.5px;line-height:22px;color:var(--body)}
.featured .features{color:var(--white)}
.features li::before{content:"✓";color:var(--teal);margin-right:7px;font-weight:700}
.featured .features li::before{color:var(--white)}
.features li.off::before{content:"✕";color:var(--muted)}
.price-btn{position:absolute;left:50%;transform:translateX(-50%);bottom:48px;font-size:8.5px;font-weight:700;letter-spacing:1px;padding:11px 17px;background:var(--teal);color:var(--white);border-radius:2px}
.featured .price-btn{background:var(--white);color:var(--teal);bottom:50px}

/* footer */
.footer-band{left:0;top:3290px}
.foot-brand{left:241px;top:3452px;display:flex;align-items:center;gap:8px;color:var(--white);font-weight:700;font-size:13px}
.foot-col{top:3452px;color:var(--white)}
.foot-col h4{font-size:11px;font-weight:600;letter-spacing:1px;text-transform:uppercase;margin-bottom:20px}
.foot-col p{font-size:9.5px;line-height:16px}
.foot-rule{height:1px;background:rgba(255,255,255,.4);margin:14px 0}
.foot-links{display:grid;grid-template-columns:95px 95px;font-size:9.5px;line-height:20px}
.copyright{left:241px;top:3660px;font-size:9px;color:var(--white)}
.socials{left:884px;top:3660px;display:flex;gap:10px}
.socials i{width:9px;height:9px;border-radius:50%;background:rgba(255,255,255,.85);display:block}
</style>
</head>
<body>

<!-- Hero -->
<section class="hero abs">
  <div class="hero-photo" role="img" aria-label="Photo of two people holding a plank on grass in a sunlit park"></div>
  <div class="hero-shade"></div>
  <svg class="hero-wave" width="1200" height="665" viewBox="0 0 1200 665">
    <path d="M0 600 C120 540 220 515 330 518 C470 522 560 610 700 640 C820 665 900 610 1000 560 C1080 520 1150 520 1200 540 L1200 665 L0 665 Z" fill="#ffffff"/>
  </svg>
</section>

<nav class="nav abs">
  <div class="brand abs"><span class="brand-dot"></span>The Lantern</div>
  <div class="nav-links abs">
    <span>Home</span><span>About Us</span><span>Services</span><span>Testimonials</span><span>Plans</span>
    <span class="btn btn-teal">Get Started</span>
  </div>
</nav>

<h1 class="hero-title abs">Make healthy lifestyle changes</h1>
<p class="hero-sub abs">Lorem ipsum dolor sit amet, consectetur adipiscing elit, sed do eiusmod tempor incididunt pers unde omnis iste natus voluptatem</p>
<div class="hero-cta abs">
  <span class="btn btn-teal">Get Started</span>
  <span class="btn btn-ghost">Learn More</span>
</div>

<!-- About -->
<h2 class="about-title abs">Aim to lose weight and gain strenght?</h2>
<div class="about-rule abs"></div>
<p class="about-text abs" style="top:934px">Lorem ipsum dolor sit amet, consectetur adipiscing elit, sed do eiusmod tempor incididunt ut labore et dolore magna aliqua. Ut enim ad minim veniam, quis nostrud exercitation ullamco laboris nisi ut aliquip ex ea commodo consequat.</p>
<p class="about-text abs" style="top:1012px">Duis aute irure dolor in reprehenderit in voluptate velit esse cillum dolore eu fugiat nulla pariatur. Excepteur sint occaecat cupidatat non proident, sunt in culpa qui officia deserunt mollit anim id est laborum.</p>
<div class="about-frame abs"></div>
<div class="about-photo abs" role="img" aria-label="Photo of a hiker crossing a suspension bridge toward mountains at sunrise"></div>

<!-- Services -->
<svg class="services-band abs" width="1200" height="740" viewBox="0 0 1200 740">
  <defs>
    <linearGradient id="bandGrad" x1="0" y1="0" x2="1" y2="0.3">
      <stop offset="0" stop-color="#74c6f7"/>
      <stop offset="1" stop-color="#6a63f4"/>
    </linearGradient>
  </defs>
  <path d="M0 680 C200 720 350 740 560 700 C800 655 1000 610 1200 600 L1200 625 C1000 640 800 690 560 720 C350 745 200 735 0 700 Z" fill="#d9d2fb"/>
  <path d="M0 62 C140 10 260 5 420 20 C640 40 760 120 940 125 C1060 128 1140 115 1200 100 L1200 610 C1000 620 800 665 560 700 C350 730 200 715 0 690 Z" fill="url(#bandGrad)"/>
</svg>

<header class="services-head abs">
  <p class="eyebrow">Lorem Ipsum</p>
  <h2 class="section-title">Our Services</h2>
</header>

<article class="card abs" style="left:241px;top:1473px">
  <span class="card-tab"></span>
  <svg class="card-icon" width="32" height="32" viewBox="0 0 32 32" fill="none" stroke="#3cc3cc" stroke-width="1.6"><rect x="4" y="5" width="24" height="17" rx="1"/><path d="M10 27h12M16 22v5M10 15l4-4 4 4 4-5"/></svg>
  <h3>Online trainer</h3>
  <p>Lorem ipsum dolor sit amet, consectetur adipiscing elit, sed do eiusmod tempor incididunt ut labore magna</p>
</article>
<article class="card abs" style="left:488px;top:1473px">
  <span class="card-tab"></span>
  <svg class="card-icon" width="32" height="32" viewBox="0 0 32 32" fill="none" stroke="#3cc3cc" stroke-width="1.6"><rect x="4" y="5" width="24" height="17" rx="1"/><path d="M10 27h12M16 22v5M10 15l4-4 4 4 4-5"/></svg>
  <h3>Strength &amp; Conditioning</h3>
  <p>Lorem ipsum dolor sit amet, consectetur adipiscing elit, sed do eiusmod tempor incididunt ut labore magna</p>
</article>
<article class="card abs" style="left:734px;top:1473px">
  <span class="card-tab"></span>
  <svg class="card-icon" width="32" height="32" viewBox="0 0 32 32" fill="none" stroke="#3cc3cc" stroke-width="1.6"><rect x="4" y="5" width="24" height="17" rx="1"/><path d="M10 27h12M16 22v5M10 15l4-4 4 4 4-5"/></svg>
  <h3>Lorem Ipsum Dolor</h3>
  <p>Lorem ipsum dolor sit amet, consectetur adipiscing elit, sed do eiusmod tempor incididunt ut labore magna</p>
</article>
<article class="card abs" style="left:241px;top:1737px">
  <span class="card-tab"></span>
  <svg class="card-icon" width="32" height="32" viewBox="0 0 32 32" fill="none" stroke="#3cc3cc" stroke-width="1.6"><rect x="4" y="5" width="24" height="17" rx="1"/><path d="M10 27h12M16 22v5M10 15l4-4 4 4 4-5"/></svg>
  <h3>Online trainer</h3>
  <p>Lorem ipsum dolor sit amet, consectetur adipiscing elit, sed do eiusmod tempor incididunt ut labore magna</p>
</article>
<article class="card abs" style="left:488px;top:1737px">
  <span class="card-tab"></span>
  <svg class="card-icon" width="32" height="32" viewBox="0 0 32 32" fill="none" stroke="#3cc3cc" stroke-width="1.6"><rect x="4" y="5" width="24" height="17" rx="1"/><path d="M10 27h12M16 22v5M10 15l4-4 4 4 4-5"/></svg>
  <h3>Strength &amp; Conditioning</h3>
  <p>Lorem ipsum dolor sit amet, consectetur adipiscing elit, sed do eiusmod tempor incididunt ut labore magna</p>
</article>
<article class="card abs" style="left:734px;top:1737px">
  <span class="card-tab"></span>
  <svg class="card-icon" width="32" height="32" viewBox="0 0 32 32" fill="none" stroke="#3cc3cc" stroke-width="1.6"><rect x="4" y="5" width="24" height="17" rx="1"/><path d="M10 27h12M16 22v5M10 15l4-4 4 4 4-5"/></svg>
  <h3>Lorem Ipsum Dolor</h3>
  <p>Lorem ipsum dolor sit amet, consectetur adipiscing elit, sed do eiusmod tempor incididunt ut labore magna</p>
</article>

<!-- Testimonials -->
<section class="testi-box abs"></section>
<header class="testi-head abs">
  <p class="eyebrow">Our Clients</p>
  <h2 class="section-title">Testimonials</h2>
</header>
<div class="quote-mark abs">“</div>
<p class="testi-lead abs">Lorem ipsum dolor sit amet, consectetur adipiscing</p>
<p class="testi-text abs">Sed ut perspiciatis unde omnis iste natus error sit voluptatem accusantium doloremque laudantium, totam rem aperiam, eaque ipsa quae ab illo inventore veritatis et quasi architecto beatae vitae dicta sunt explicabo. Nemo enim ipsam voluptatem quia voluptas sit aspernatur aut odit aut fugit, sed quia consequuntur magni dolores eos qui ratione voluptatem.</p>
<div class="avatar abs" role="img" aria-label="Client portrait"></div>
<p class="testi-name abs">Jordan Reyes <span>Sport Trainer</span></p>

<!-- Pricing -->
<header class="abs" style="left:0;width:1200px;top:2648px">
  <p class="eyebrow">Our Plans</p>
  <h2 class="section-title" style="margin-top:6px">Our Pricing</h2>
</header>

<div class="price-card abs" style="left:241px;width:227px">
  <p class="plan">Beginner</p>
  <p class="amount">Free</p>
  <p class="per">Always</p>
  <div class="divider"></div>
  <ul class="features"><li>Lorem ipsum dolor</li><li>Adipiscing elit</li><li>Lorem ips dolor</li><li>Excepteur sint prident</li><li class="off">Duis aute</li></ul>
  <span class="price-btn">SUBSCRIBE</span>
</div>
<div class="price-card featured abs" style="left:468px;width:264px">
  <p class="plan" style="margin-top:36px">Most Popular</p>
  <p class="amount">$17<sup>90</sup></p>
  <p class="per">Per Month</p>
  <div class="divider"></div>
  <ul class="features"><li>Lorem ipsum dolor</li><li>Adipiscing elit</li><li>Lorem ips dolor</li><li>Excepteur sint prident</li><li>Duis aute</li></ul>
  <span class="price-btn">SUBSCRIBE</span>
</div>
<div class="price-card abs" style="left:732px;width:226px">
  <p class="plan">Advanced</p>
  <p class="amount">$48<sup>90</sup></p>
  <p class="per">Per Month</p>
  <div class="divider"></div>
  <ul class="features"><li>Lorem ipsum dolor</li><li>Adipiscing elit</li><li>Lorem ips dolor</li><li>Excepteur sint prident</li><li class="off">Duis aute</li></ul>
  <span class="price-btn">SUBSCRIBE</span>
</div>

<!-- Footer -->
<svg class="footer-band abs" width="1200" height="406" viewBox="0 0 1200 406">
  <defs>
    <linearGradient id="footGrad" x1="0" y1="0" x2="1" y2="0.4">
      <stop offset="0" stop-color="#74c6f7"/>
      <stop offset="1" stop-color="#6a63f4"/>
    </linearGradient>
  </defs>
  <path d="M0 60 C150 40 260 70 380 80 C520 92 640 40 780 22 C900 6 1000 20 1080 40 C1140 55 1180 60 1200 58 L1200 406 L0 406 Z" fill="url(#footGrad)"/>
</svg>

<div class="foot-brand abs"><span class="brand-dot" style="background:#ffffff"></span>The Lantern</div>

<div class="foot-col abs" style="left:547px;width:140px">
  <h4>Contact Us</h4>
  <p>Your address, South Florida,<br>office 301</p>
  <div class="foot-rule"></div>
  <p>P: +1 305-555-0148</p>
  <p>E: hello@lanternclub.com</p>
</div>

<div class="foot-col abs" style="left:793px;width:200px">
  <h4>Learn More</h4>
  <div class="foot-links">
    <span>Lorem ipsum</span><span>Lorem ipsum</span>
    <span>Dolor sit amet</span><span>Dolor sit amet</span>
    <span>Duis aute irure</span><span>Duis aute irure</span>
    <span>Nemo ipsam</span><span>Nemo ipsam</span>
  </div>
</div>

<p class="copyright abs">© 2019 The Lantern Athletic Club All Rights Reserved</p>
<div class="socials abs"><i></i><i></i><i></i><i></i></div>

</body>
</html>
```